Safety Work Area Signage to keep people away from work zone

We would like to create a simple design that will include our logo and phone number, 'work area', and 'caution / cuidado' (please see a mock-up of the intended design in the uploaded files). Please provide multiple options. We would like a Professional look for the poster as it is meant for safety. Poster Size to be: 18.16" X 23.10"

Target Market(s)

General Public on Construction Sites

Font styles to use
Serif

Requirements
Must have
• see mock-ups in uploaded files
Nice to have
• Simple Design, Professional Look

```html
<!DOCTYPE html>
<html lang="en">
<head>
<meta charset="utf-8">
<title>Work Area Safety Signs</title>
<link href="https://fonts.googleapis.com/css2?family=Arimo:wght@700&family=Bitter:wght@700&display=swap" rel="stylesheet">
<style>
  :root {
    --backdrop: #5e5e5e;
    --sign-red: #ff3131;
    --band-dark: #262626;
    --ink: #1c1c1c;
    --paper: #ffffff;
  }
  * { box-sizing: border-box; margin: 0; padding: 0; }
  html, body {
    width: 1200px; height: 878px; overflow: hidden;
    background: var(--backdrop);
  }
  .canvas { position: relative; width: 1200px; height: 878px; }
  .sign {
    position: absolute; top: 113px; width: 515px; height: 656px;
    background: var(--sign-red);
    box-shadow: 0 4px 10px rgba(0,0,0,.35);
    overflow: hidden;
  }
  .sign--banner { left: 63px; }
  .sign--badge { left: 626px; }

  .hazard-stripes {
    position: absolute; left: 0; width: 100%; height: 14px;
    background: repeating-linear-gradient(125deg,
      var(--sign-red) 0 9px, var(--band-dark) 9px 21px, var(--sign-red) 21px 26px);
  }
  .hazard-stripes--top { top: 10px; }
  .hazard-stripes--mid { top: 137px; }
  .hazard-stripes--bottom { top: 642px; }

  .caution-band {
    position: absolute; top: 31px; left: 0; width: 100%; height: 99px;
    background: var(--band-dark);
  }
  .caution-icon { position: absolute; left: 34px; top: 13px; width: 77px; height: 69px; }
  .caution-word {
    position: absolute; left: 131px; top: 18px;
    font-family: "Arimo", Arial, sans-serif; font-weight: 700;
    font-size: 68px; line-height: 68px; color: var(--paper);
    white-space: nowrap;
  }

  .headline {
    position: absolute; left: 0; width: 100%; text-align: center;
    font-family: "Arimo", Arial, sans-serif; font-weight: 700;
    color: var(--paper);
    text-shadow: 3px 3px 0 var(--ink);
    white-space: nowrap;
  }
  .headline--work { top: 158px; font-size: 102px; line-height: 102px; }
  .headline--area { top: 248px; font-size: 102px; line-height: 102px; }
  .headline--spanish { top: 556px; font-size: 82px; line-height: 82px; }

  .phone {
    position: absolute; left: 0; width: 100%; top: 514px; text-align: center;
    font-family: "Arimo", Arial, sans-serif; font-weight: 700;
    font-size: 40px; line-height: 40px; color: var(--paper);
    text-shadow: 2px 2px 0 var(--ink);
    white-space: nowrap;
  }

  .company-panel {
    position: absolute; left: 0; top: 364px; width: 100%; height: 138px;
    background: var(--paper);
    border-top: 4px solid var(--band-dark);
    border-bottom: 4px solid var(--band-dark);
    font-family: "Bitter", Georgia, serif; font-weight: 700; color: var(--ink);
  }
  .company-name {
    position: absolute; left: 40px; top: 14px; width: 200px;
    font-size: 28px; line-height: 33px; text-align: center;
  }
  .company-divider {
    position: absolute; left: 247px; top: 12px; width: 2px; height: 66px;
    background: var(--ink);
  }
  .company-trade {
    position: absolute; left: 262px; top: 12px; width: 220px;
    font-size: 29px; line-height: 31px; text-align: center;
  }
  .company-motto {
    position: absolute; left: 0; width: 100%; top: 86px;
    font-size: 25px; line-height: 32px; text-align: center;
  }

  .company-badge {
    position: absolute; left: 163px; top: 344px; width: 164px; height: 164px;
    border-radius: 50%; background: var(--paper);
    display: flex; align-items: center; justify-content: center;
    font-family: "Bitter", Georgia, serif; font-weight: 700; color: var(--ink);
    font-size: 22px; line-height: 28px; text-align: center;
  }
</style>
</head>
<body>
<main class="canvas">
  <section class="sign sign--banner">
    <div class="hazard-stripes hazard-stripes--top"></div>
    <div class="caution-band">
      <svg class="caution-icon" viewBox="0 0 77 69" aria-hidden="true">
        <path d="M38.5 3 L74 64 Q75 67 71 67 L6 67 Q2 67 3 64 Z" fill="#fff" stroke="#fff" stroke-width="4" stroke-linejoin="round"/>
        <rect x="34" y="22" width="10" height="26" fill="#262626"/>
        <rect x="34" y="53" width="10" height="9" fill="#262626"/>
      </svg>
      <div class="caution-word">CAUTION</div>
    </div>
    <div class="hazard-stripes hazard-stripes--mid"></div>
    <div class="headline headline--work">WORK</div>
    <div class="headline headline--area">AREA</div>
    <div class="company-panel">
      <div class="company-name">Harlow &amp; Pierce, Inc.</div>
      <div class="company-divider"></div>
      <div class="company-trade">General Contractors</div>
      <div class="company-motto">“Built Right, Built Safe”</div>
    </div>
    <div class="phone">(555) 014-2290</div>
    <div class="headline headline--spanish" lang="es">CUIDADO</div>
    <div class="hazard-stripes hazard-stripes--bottom"></div>
  </section>

  <section class="sign sign--badge">
    <div class="hazard-stripes hazard-stripes--top"></div>
    <div class="caution-band">
      <svg class="caution-icon" viewBox="0 0 77 69" aria-hidden="true">
        <path d="M38.5 3 L74 64 Q75 67 71 67 L6 67 Q2 67 3 64 Z" fill="#fff" stroke="#fff" stroke-width="4" stroke-linejoin="round"/>
        <rect x="34" y="22" width="10" height="26" fill="#262626"/>
        <rect x="34" y="53" width="10" height="9" fill="#262626"/>
      </svg>
      <div class="caution-word">CAUTION</div>
    </div>
    <div class="hazard-stripes hazard-stripes--mid"></div>
    <div class="headline headline--work">WORK</div>
    <div class="headline headline--area">AREA</div>
    <div class="company-badge">Harlow &amp;<br>Pierce, Inc.</div>
    <div class="phone">(555) 014-2290</div>
    <div class="headline headline--spanish" lang="es">CUIDADO</div>
    <div class="hazard-stripes hazard-stripes--bottom"></div>
  </section>
</main>
</body>
</html>
```